Product page for a pain diary needs an impressive Pressory Design

We are a small startup from Switzerland, called Belquira AG (see www.belquira-example.com). We are developing an application "TrackWillow" which will be launched end of December/January. So far we only had a landing-page: www.trackwillow-example.com and now want to extend it to a complete website.

Our upcoming app is a diary which can be used by chronic pain patients to track their pain over time. Towards the end of this December we are going to launch a tablet app on Zelix/norvane. A few months later a smartphone version and a desktop browser version will follow.

We think our product page should have 5 pages/categories:
- start page: there will be a video, some testimonials and links to app bazaar and fennel market
- details: We explain why you should keep a diary and what TrackWillow is? This page includes some screenshots of the application
- vision: we present our roadmap and our quest against pain
- FAQ: most important questions answered, links to support, includes a form as well
- about: link to belquira-example.com-page, descriptions of who we are, team-picture

Here are some additional remarks:
- some pages/categories could have subpages at a later point. Please keep this in mind when designing the webpage.

- somewhere one the webpage, there should be a chirpnet-feed integrated "@TrackWillow"

- The Webpage should run in a multiple-language mode. Currently, we are using the multiple language framework at http://plugvault-example.org/extend/plugins/polytongue-kit/ and have the site in German and English. The site design can be in one language only, but should there be graphics with text, we would need both versions. Ideally, you provide us with the “raw” format in addition. This way we can change the text ourselves.

- chronic pain is a serious (and oftentimes sad topic). However, the design should represent a positive attitude (hope) while appearing professional.
- You can reuse the color scheme of our TrackWillow logo. However, we are also open to new color suggestions.
Updates

I added some newer screenshots from inside the application. The ones now existing on trackwillow-example.com are a bit old already.

general notes for all:
- only use official black / white (transparent) appBazaar icons, others aren't allowed by quince
- use newer screenshots for drafts (see brief)
- always have a navigation
- video should be prominent (size can be expanded upon click)
- main-page without slideshow (one static element is enough)
- different screenshots can still be used on other pages

most important items (things that should be seen at first glance without scrolling):
- screenshot
- appbazaar icons
- video
(- newsletter subscription)

generally we would like to have
- not too much black parts on the page, it can be fresh and friendly ;)
- no pics in background that have nothing to do with TrackWillow

Target Market(s)

Average app/web user who suffers from (chronic) pain

Industry/Entity Type

Store

Requirements
Must have
• - quick links to download the application from appstores
- newsletter subscription box, to subscribe with email-address
- support for English/German

- delivery as a Pressory Theme/Plugin
Nice to have
• - an alternate styling for mobile version of the website.

```html
<!DOCTYPE html>
<html lang="en">
<head>
<meta charset="utf-8">
<title>TrackWillow – Pain Diary</title>
<link rel="stylesheet" href="https://fonts.googleapis.com/css2?family=Oswald:wght@300;400&family=PT+Sans:ital,wght@0,400;0,700;1,400&display=swap">
<style>
  :root{
    --brand:#1ab1e6;
    --brand-dark:#0f9bd0;
    --ink:#3a3a3a;
    --muted:#777;
    --hero-bg:#eeeeee;
    --band-bg:#f2f2f2;
    --dark:#262626;
    --orange:#f39a1e;
    --white:#fff;
  }
  *{margin:0;padding:0;box-sizing:border-box}
  html,body{width:1200px;height:1157px;overflow:hidden;background:var(--white)}
  body{position:relative;font-family:"PT Sans",sans-serif;color:var(--ink)}
  .abs{position:absolute}

  /* header */
  .site-header{left:0;top:0;width:1200px;height:75px;background:var(--white);border-bottom:1px solid #e4e4e4}
  .brand{left:180px;top:20px;display:flex;align-items:center;gap:10px}
  .brand-mark{width:30px;height:30px;border-radius:50%;background:var(--brand)}
  .brand-name{font-family:"Oswald",sans-serif;font-weight:400;font-size:30px;color:var(--brand);line-height:1}
  .main-nav a{position:absolute;top:31px;transform:translateX(-50%);font-size:11px;letter-spacing:.8px;color:#555;text-decoration:none}
  .main-nav a.active{color:var(--brand)}

  /* hero */
  .hero{left:0;top:75px;width:1200px;height:343px;background:var(--hero-bg)}
  .hero-title{left:171px;top:100px;font-family:"Oswald",sans-serif;font-weight:300;font-size:45px;line-height:52px;color:#444}
  .hero-text{left:174px;top:216px;width:360px;font-size:11px;line-height:26px;letter-spacing:.8px;color:#555}
  .btn-try{left:174px;top:315px;width:137px;height:41px;background:linear-gradient(#3cc4f0,var(--brand-dark));box-shadow:2px 2px 0 #c9c9c9;color:var(--white);font-family:"Oswald",sans-serif;font-size:18px;letter-spacing:1px;text-align:center;line-height:41px}
  .store-badge{left:342px;top:314px;width:132px;height:44px;background:#000;border-radius:5px;border:1px solid #555}
  .video-frame{left:587px;top:102px;width:442px;height:275px;background:var(--white);box-shadow:0 0 4px rgba(0,0,0,.2)}
  .video-poster{left:5px;top:5px;width:432px;height:265px;background:linear-gradient(110deg,#9fb4bc 0%,#d8e6ea 40%,#eef4f6 70%,#cfe0e6 100%)}
  .play-btn{left:181px;top:93px;width:80px;height:80px}

  .dark-band{left:0;top:418px;width:1200px;height:22px;background:var(--dark)}

  /* features */
  .stripe{top:473px;height:22px;background:repeating-linear-gradient(-45deg,#bbb 0 1px,transparent 1px 4px)}
  .headline{left:506px;top:466px;width:189px;text-align:center;font-family:"Oswald",sans-serif;font-weight:300;font-size:31px;color:#444}
  .feature{top:536px;width:160px}
  .feature-icon{width:72px;height:72px;border-radius:50%;margin-left:31px}
  .feature-title{width:160px;margin-top:17px;text-align:center;font-family:"Oswald",sans-serif;font-weight:300;font-size:22px;color:#333}
  .feature-text{margin-top:12px;font-size:11px;line-height:20.6px;letter-spacing:.7px;color:var(--muted)}
  .feature-text.quote{font-style:italic}
  .author{font-size:11px;color:#222;letter-spacing:.7px;line-height:20.6px}
  .read-more{display:block;margin-top:10px;font-size:11px;letter-spacing:.8px;color:var(--brand);text-decoration:none}

  /* testimonials band */
  .testimonials{left:0;top:890px;width:1200px;height:162px;background:var(--band-bg)}
  .testimonials h2{position:absolute;left:0;top:6px;width:1200px;text-align:center;font-family:"Oswald",sans-serif;font-weight:300;font-size:22px;color:#333}
  .t-item{top:50px;width:110px}
  .t-quote{font-family:"Oswald",sans-serif;font-style:italic;font-weight:300;font-size:12px;line-height:20.6px;letter-spacing:.8px;color:#333}
  .t-author{font-size:10px;letter-spacing:.8px;color:var(--orange)}

  /* footer */
  .copyright{left:172px;top:1081px;font-size:10px;letter-spacing:.8px;color:#333}
  .social{top:1077px;width:22px;height:22px;border-radius:50%;background:linear-gradient(#f4f4f4,#d2d2d2);border:1px solid #bbb}
  .bottom-edge{left:0;top:1130px;width:1200px;height:27px}
</style>
</head>
<body>

<header class="abs site-header">
  <div class="abs brand"><span class="brand-mark"></span><span class="brand-name">TrackWillow</span></div>
  <nav class="main-nav">
    <a class="active" style="left:600px" href="#">Home</a>
    <a style="left:684px" href="#">Details</a>
    <a style="left:770px" href="#">Vision</a>
    <a style="left:847px" href="#">FAQ</a>
    <a style="left:923px" href="#">About</a>
    <a style="left:1006px" href="#">Contact</a>
  </nav>
</header>

<section class="abs hero"></section>
<h1 class="abs hero-title">Track your chronic pain<br>with our diary app</h1>
<p class="abs hero-text">Lorem ipsum dolor sit amet, consectetur adipiscing elit dolle massa felis, congue nec facilisis id, pretium congue magnathe phasellus ut orci diam, eget lobortis tellus dolor sit amet.</p>
<div class="abs btn-try">TRY NOW</div>
<div class="abs store-badge" role="img" aria-label="App bazaar download badge"></div>
<div class="abs video-frame">
  <div class="abs video-poster" role="img" aria-label="Video still: woman holding her sore neck">
    <svg class="abs play-btn" viewBox="0 0 80 80"><circle cx="40" cy="40" r="40" fill="rgba(90,90,90,.45)"/><path d="M31 25 L56 40 L31 55 Z" fill="#fff"/></svg>
  </div>
</div>

<div class="abs dark-band"></div>

<div class="abs stripe" style="left:172px;width:334px"></div>
<h2 class="abs headline">HEADLINE HERE</h2>
<div class="abs stripe" style="left:695px;width:334px"></div>

<article class="abs feature" style="left:173px">
  <div class="feature-icon" style="margin-left:32px;background:radial-gradient(circle at 55% 55%,#e86a6a,#d9d0cf 55%,#444 100%)" role="img" aria-label="Hand on painful stomach"></div>
  <h3 class="feature-title" style="margin-left:-11px">Lorem Ipsum</h3>
  <p class="feature-text">Lorem ipsum dolor sitert amet, consectetur adipisc-ing elit dolle massa feliser congue nec facilisis idiony pretium congue magnathe phasellus ut orci diam, eget lobortis tellus dolor</p>
  <a class="read-more" href="#">read more →</a>
</article>
<article class="abs feature" style="left:350px">
  <div class="feature-icon" style="margin-left:31px;background:radial-gradient(circle,#7fb2d8,#2f6fa8 70%,#fff 72%)" role="img" aria-label="X-ray of a back with pain points"></div>
  <h3 class="feature-title" style="margin-left:-14px">Lorem Ipsum</h3>
  <p class="feature-text">Lorem ipsum dolor sitert amet, consectetur adipisc-ing elit dolle massa feliser congue nec facilisis idiony pretium congue magnathe phasellus ut orci diam, eget lobortis tellus dolor</p>
  <a class="read-more" href="#">read more →</a>
</article>
<article class="abs feature" style="left:523px">
  <div class="feature-icon" style="margin-left:34px;background:radial-gradient(ellipse 40% 50%,#111 60%,#fff 62%)" role="img" aria-label="Hand holding a smartphone"></div>
  <h3 class="feature-title" style="margin-left:-9px">Lorem Ipsum</h3>
  <p class="feature-text">Lorem ipsum dolor sitert amet, consectetur adipisc-ing elit dolle massa feliser congue nec facilisis idiony pretium congue magnathe phasellus ut orci diam, eget lobortis tellus dolor</p>
  <a class="read-more" href="#">read more →</a>
</article>
<article class="abs feature" style="left:698px">
  <div class="feature-icon" style="margin-left:31px;background:linear-gradient(135deg,#cfd8de,#f1e4d8 60%,#c9d3da)" role="img" aria-label="Woman with neck pain by a window"></div>
  <h3 class="feature-title" style="margin-left:-11px">Lorem Ipsum</h3>
  <p class="feature-text">Lorem ipsum dolor sitert amet, consectetur adipisc-ing elit dolle massa feliser congue nec facilisis idiony pretium congue magnathe phasellus ut orci diam, eget lobortis tellus dolor</p>
  <a class="read-more" href="#">read more →</a>
</article>
<article class="abs feature" style="left:880px">
  <div class="feature-icon" style="margin-left:31px;background:radial-gradient(circle at 50% 45%,#9aa,#333 60%,#111)" role="img" aria-label="X-ray of a shoulder joint"></div>
  <h3 class="feature-title" style="margin-left:-13px">Testimonials</h3>
  <p class="feature-text quote">“Lorem ipsum dolor sitert amet, consectetur adipisc-ing elit dolle massa feliser congue nec facilisis idiony pretium congue magnathe phasellus ut orci diam”</p>
  <div class="author">Nora Lindqvist, Company</div>
  <a class="read-more" href="#">read more →</a>
</article>

<section class="abs testimonials">
  <h2>Testimonials</h2>
  <div class="abs t-item" style="left:172px"><p class="t-quote">“Lorem ipsum dolsit amet, con-sectetur adipisc-ing eli reedit”</p><div class="t-author">Mr Lorem Ipsum</div></div>
  <div class="abs t-item" style="left:326px"><p class="t-quote">“Lorem ipsum dolsit amet, con-sectetur adipisc-ing eli reedit”</p><div class="t-author">Mr Lorem Ipsum</div></div>
  <div class="abs t-item" style="left:476px"><p class="t-quote">“Lorem ipsum dolsit amet, con-sectetur adipisc-ing eli reedit”</p><div class="t-author">Mr Lorem Ipsum</div></div>
  <div class="abs t-item" style="left:642px"><p class="t-quote">“Lorem ipsum dolsit amet, con-sectetur adipisc-ing eli reedit”</p><div class="t-author">Mr Lorem Ipsum</div></div>
  <div class="abs t-item" style="left:793px"><p class="t-quote">“Lorem ipsum dolsit amet, con-sectetur adipisc-ing eli reedit”</p><div class="t-author">Mr Lorem Ipsum</div></div>
  <div class="abs t-item" style="left:947px"><p class="t-quote">“Lorem ipsum dolsit amet, con-sectetur adipisc-ing eli reedit”</p><div class="t-author">Mr Lorem Ipsum</div></div>
</section>

<footer>
  <p class="abs copyright">© Copyright 2012 TrackWillow | Back to top ▴</p>
  <span class="abs social" style="left:931px" aria-label="Social link"></span>
  <span class="abs social" style="left:967px" aria-label="Social link"></span>
  <span class="abs social" style="left:1004px" aria-label="Feed link"></span>
  <svg class="abs bottom-edge" viewBox="0 0 1200 27" preserveAspectRatio="none">
    <path d="M0 27 V4 L5 0 L10 4 L15 0 L20 4 L25 0 L30 4 L35 0 L40 4 L45 0 L50 4 L55 0 L60 4 L65 0 L70 4 L75 0 L80 4 L85 0 L90 4 L95 0 L100 4 L105 0 L110 4 L115 0 L120 4 L125 0 L130 4 L135 0 L140 4 L145 0 L150 4 L155 0 L160 4 L165 0 L170 4 L175 0 L180 4 L185 0 L190 4 L195 0 L200 4 L205 0 L210 4 L215 0 L220 4 L225 0 L230 4 L235 0 L240 4 L245 0 L250 4 L255 0 L260 4 L265 0 L270 4 L275 0 L280 4 L285 0 L290 4 L295 0 L300 4 L305 0 L310 4 L315 0 L320 4 L325 0 L330 4 L335 0 L340 4 L345 0 L350 4 L355 0 L360 4 L365 0 L370 4 L375 0 L380 4 L385 0 L390 4 L395 0 L400 4 L405 0 L410 4 L415 0 L420 4 L425 0 L430 4 L435 0 L440 4 L445 0 L450 4 L455 0 L460 4 L465 0 L470 4 L475 0 L480 4 L485 0 L490 4 L495 0 L500 4 L505 0 L510 4 L515 0 L520 4 L525 0 L530 4 L535 0 L540 4 L545 0 L550 4 L555 0 L560 4 L565 0 L570 4 L575 0 L580 4 L585 0 L590 4 L595 0 L600 4 L605 0 L610 4 L615 0 L620 4 L625 0 L630 4 L635 0 L640 4 L645 0 L650 4 L655 0 L660 4 L665 0 L670 4 L675 0 L680 4 L685 0 L690 4 L695 0 L700 4 L705 0 L710 4 L715 0 L720 4 L725 0 L730 4 L735 0 L740 4 L745 0 L750 4 L755 0 L760 4 L765 0 L770 4 L775 0 L780 4 L785 0 L790 4 L795 0 L800 4 L805 0 L810 4 L815 0 L820 4 L825 0 L830 4 L835 0 L840 4 L845 0 L850 4 L855 0 L860 4 L865 0 L870 4 L875 0 L880 4 L885 0 L890 4 L895 0 L900 4 L905 0 L910 4 L915 0 L920 4 L925 0 L930 4 L935 0 L940 4 L945 0 L950 4 L955 0 L960 4 L965 0 L970 4 L975 0 L980 4 L985 0 L990 4 L995 0 L1000 4 L1005 0 L1010 4 L1015 0 L1020 4 L1025 0 L1030 4 L1035 0 L1040 4 L1045 0 L1050 4 L1055 0 L1060 4 L1065 0 L1070 4 L1075 0 L1080 4 L1085 0 L1090 4 L1095 0 L1100 4 L1105 0 L1110 4 L1115 0 L1120 4 L1125 0 L1130 4 L1135 0 L1140 4 L1145 0 L1150 4 L1155 0 L1160 4 L1165 0 L1170 4 L1175 0 L1180 4 L1185 0 L1190 4 L1195 0 L1200 4 V27 Z" fill="var(--dark)"/>
  </svg>
</footer>

</body>
</html>
```